Report layout - design layout for automatic welcome letter PDF

We need to design the layout for a welcome letter PDF being automatically generated by an Enterprise web application.
We give you the ugly Ms. Word layout, we need to create a nice template for the same content to be automatically generated in PDF.
In particular we attached:
Reason: Hi guys,
I was unfortunately sick in the last few days and I could not work on the designs feedback. Now I am back, please apologize.
I am extending the deadline of 5 days in order to sort things out.
I want to thank you guys already for nice design received!
Teodoro
Target Market(s)
Enterprise business.
Industry/Entity Type
Bank
Requirements
Must have
- 1) Front page with customer details;
- 2) Second page: legal notice.
- If it turns out that we do not fit in 2 pages we can even make 3, but I would keep legal notice separated from customer details.
Nice to have
- 1) Header and footer that makes it easy to create it automatically using PDF.
- 2) You will see that logo and application are using different types of red. I believe we can uniform them. If you have inspiration regarding the logo feel free to suggest.

```html
<!DOCTYPE html>
<html lang="it">
<head>
<meta charset="utf-8">
<title>LoomStoreVault – Modulo di attivazione e NDA</title>
<link rel="stylesheet" href="https://fonts.googleapis.com/css2?family=Montserrat:wght@500;700;800&family=Lato:ital,wght@0,400;0,700;1,700&display=swap">
<style>
:root{
  --backdrop:#7a8b38;
  --paper:#ffffff;
  --brand-red:#e3233f;
  --brand-pink:#f28a9b;
  --tab-grey:#8e8e8e;
  --line-grey:#8a8a8a;
  --ink:#1c1c1c;
  --muted:#7a7a7a;
}
*{box-sizing:border-box;margin:0;padding:0}
html,body{width:1200px;height:834px;overflow:hidden;background:var(--backdrop)}
body{position:relative;font-family:"Lato",Arial,sans-serif;color:var(--ink)}
.page{position:absolute;top:18px;width:563px;height:797px;background:var(--paper);overflow:hidden}
.page--activation{left:23px}
.page--nda{left:610px}

.brand{position:absolute;top:26px;left:0;width:100%;text-align:center}
.brand__name{font-family:"Montserrat",sans-serif;font-weight:500;font-size:22px;letter-spacing:-.3px;color:#2a2a2a;line-height:1}
.brand__url{font-family:"Montserrat",sans-serif;font-weight:500;font-size:13.5px;color:var(--brand-red);line-height:1.2}

.title-bar{position:absolute;left:34px;width:496px;top:72px;height:43px;background:var(--brand-red);color:#fff;
  font-family:"Montserrat",sans-serif;font-weight:800;font-size:16px;display:flex;align-items:center;justify-content:center;letter-spacing:.2px;white-space:nowrap}
.title-bar small{font-weight:700;font-size:14px;margin-left:4px}
.title-note{position:absolute;left:34px;width:496px;top:115px;border:2px solid var(--brand-red);border-top:0;
  text-align:center;font-family:"Montserrat",sans-serif;font-weight:700;font-size:12px;line-height:16px}
.title-note--intro{height:58px;padding-top:12px}
.title-note--date{height:28px;padding-top:6px;font-family:"Lato",sans-serif;font-size:11px;line-height:14px;white-space:nowrap;overflow:hidden}

.section{position:absolute;left:37px;width:490px;border:2px solid var(--line-grey);border-top:0}
.section::before{content:"";position:absolute;left:-2px;right:-2px;top:8px;border-top:2px solid var(--line-grey)}
.section__tab{position:absolute;left:-2px;top:0;height:27px;background:var(--tab-grey);color:#fff;
  font-family:"Montserrat",sans-serif;font-weight:700;font-size:11px;padding:6px 7px;z-index:1;letter-spacing:.2px;white-space:nowrap}
.fields{position:absolute;left:6px;right:6px;top:33px;font-size:8.5px}
.field{display:grid;grid-template-columns:131px 1fr;line-height:14px}
.field b{font-family:"Montserrat",sans-serif;font-weight:700;font-size:8.8px}
.section__hint{position:absolute;right:6px;bottom:3px;font-size:7.5px;color:var(--muted)}

.customer{top:189px;height:91px}
.contract{top:299px;height:143px}
.users{top:457px;height:109px}
.users .section__hint{left:0;right:0;text-align:center;border-top:2px solid var(--line-grey);bottom:0;height:17px;padding-top:3px;font-size:8.5px}
.providers{position:absolute;left:298px;top:0;width:190px;height:88px;background:#a3a3a3;color:#3a3a3a;text-align:center;font-size:7.8px;line-height:11px;padding:4px 6px;z-index:2}
.providers h3{font-size:9px;font-weight:700;color:#111;margin-bottom:8px}
.providers p{margin-bottom:5px}

.signoff{top:579px;height:154px}
.signoff .col{position:absolute;top:33px;font-size:9px;line-height:15px}
.signoff .col h4{font-family:"Montserrat",sans-serif;font-weight:800;font-size:9.5px;margin-bottom:11px}
.col--customer{left:4px;width:220px}
.col--vault{left:272px;width:214px}
.sign-line{position:absolute;left:0;width:100%;display:flex;font-family:"Montserrat",sans-serif;font-weight:700;font-size:9px}
.sign-line span{flex:1;border-bottom:1px solid #333;margin-left:6px;margin-bottom:3px}
.sign-line--date{top:73px}
.sign-line--sign{top:90px}

.footer{position:absolute;left:0;bottom:0;width:100%;height:58px;background:var(--brand-red);color:#fff;text-align:center;font-size:8.5px;line-height:16px;padding-top:11px}
.footer::before{content:"";position:absolute;left:0;right:0;top:-4px;height:4px;background:var(--brand-pink)}
.footer strong{font-family:"Montserrat",sans-serif;font-weight:700}
.footer .gap{display:inline-block;width:22px}

.party{top:150px;height:74px}
.party .fields{top:23px}
.counterparty{top:232px;height:338px}
.counterparty .section__tab{width:42px}
.counterparty__head{position:absolute;left:44px;top:8px;font-size:7.8px;font-weight:700;padding-top:4px;white-space:nowrap}
.nda-text{position:absolute;left:6px;right:6px;top:42px;font-size:7.2px;line-height:10.2px;text-align:justify;color:#222}
.nda-text p{margin-bottom:9px}
.nda-text ul{margin:-4px 0 9px 18px}
.nda-text li{font-weight:700;font-style:italic}
.blank{display:inline-block;width:138px;border-bottom:1px solid #333}
</style>
</head>
<body>

<section class="page page--activation">
  <header class="brand">
    <div class="brand__name">LOOM STORE VAULT</div>
    <div class="brand__url">www.loomstorevault.net</div>
  </header>
  <div class="title-bar">MODULO DI ATTIVAZIONE: CONTRATTO E CLIENTE</div>
  <div class="title-note title-note--intro">Con la presente si certifica l’avvenuta attivazione del contratto di<br>cancellazione&nbsp; sicura dei dati secondo le indicazioni che seguono</div>

  <div class="section customer">
    <div class="section__tab" style="width:175px">Committente (CUSTOMER)</div>
    <div class="fields">
      <div class="field"><span></span><b>Veltrano Servizi Italia s.p.a.</b></div>
      <div class="field"><span>P.IVA:</span><b>98765432100</b></div>
      <div class="field"><span>Contatto di riferimento:</span><b>Marco Ferretti</b></div>
    </div>
    <div class="section__hint">[aggiungere le informazioni presenti nel modulo di richiesta anagrafica]</div>
  </div>

  <div class="section contract">
    <div class="section__tab" style="width:175px">Dati del Contratto</div>
    <div class="fields" style="top:28px">
      <div class="field"><span></span><b>34194-21</b></div>
      <div class="field"><span>Titolo:</span><b>Veltrano service 2014</b></div>
      <div class="field"><span>Descrizione:</span><b>Lavorazioni di cancellazione per clienti VELTRANO</b></div>
      <div class="field"><span>Data inizio e fine:</span><b>2014-07-01/---</b></div>
      <div class="field"><span>Procedura di cancellazione:</span><b>Standard Data Wipe</b></div>
      <div class="field"><span>Metodo di cancellazione:</span><b>HMG Infosec Standard N:5 (enhanced)</b></div>
      <div class="field"><span>In caso di dischi guasti:</span><b>Degaussing+Triturazione</b></div>
    </div>
    <div class="section__hint">Le ISO di cancellazione saranno disponibili…..</div>
  </div>

  <div class="section users">
    <div class="section__tab" style="width:172px">Utenti abilitati</div>
    <div class="providers">
      <h3>Ulteriori PROVIDER Abilitati:</h3>
      <p>Il presente contratto è stato abilitata ai PROVIDER che seguono.</p>
      <p>Per ciascun PROVIDER riferirsi al modulo P di attivazione corrispondente.</p>
    </div>
    <div class="fields">
      <div class="field"><span></span><b>Marco Ferretti</b></div>
      <div class="field"><span>@:</span><b>marco.ferretti@veltrano.it</b></div>
      <div class="field"><span>Telefono:</span><b>3401122334</b></div>
    </div>
    <div class="section__hint">Nessun ulteriore provider attivato.</div>
  </div>

  <div class="section signoff">
    <div class="section__tab" style="width:172px">Letto e accettato da:</div>
    <div class="col col--customer">
      <h4>CUSTOMER</h4>
      <div class="sign-line sign-line--date">Data<span></span></div>
      <div class="sign-line sign-line--sign">Firma<span></span></div>
    </div>
    <div class="col col--vault">
      <h4>LSV</h4>
      Luca Bernardi<br>Amministratore Unico<br>Orbis Data Services srl
      <div class="sign-line sign-line--date">Data<span></span></div>
      <div class="sign-line sign-line--sign">Firma<span></span></div>
    </div>
  </div>

  <footer class="footer">
    <strong>Orbis Data Services srl</strong>, Via Galvani 12/B, 20089 - Rozzano (MI)<br>
    Telefono: <strong>+39 02 55501234</strong><span class="gap"></span>info@loomstorevault.net<span class="gap"></span><strong>www.loomstorevault.net</strong>
  </footer>
</section>

<section class="page page--nda">
  <header class="brand">
    <div class="brand__name">LOOM STORE VAULT</div>
    <div class="brand__url">www.loomstorevault.net</div>
  </header>
  <div class="title-bar">ACCORDO DI SEGRETEZZA <small>(Non Disclosure Agreement)</small></div>
  <div class="title-note title-note--date">Questo accordo è stato redatto il giorno [&nbsp; 3&nbsp; ] del mese di&nbsp; [&nbsp;&nbsp; Febbraio&nbsp;&nbsp; ] Duemilaundici</div>

  <div class="section party">
    <div class="section__tab" style="width:42px">TRA</div>
    <div class="fields">
      <div class="field"><span></span><b>Veltrano Servizi Italia s.p.a.</b></div>
      <div class="field"><span>P.IVA:</span><b>98765432100</b></div>
      <div class="field"><span>Contatto di riferimento:</span><b>Marco Ferretti</b></div>
    </div>
  </div>

  <div class="section counterparty">
    <div class="section__tab">e</div>
    <div class="counterparty__head">2. Orbis Data Services srl, con sede legale in Via Galvani, 12/B, Rozzano, Milano, Italia.</div>
    <div class="nda-text">
      <p><span class="blank"></span>e Orbis Data Services srl si accordano per dare l’un l’altro alcune informazioni confidenziali, non pubbliche, al solo scopo di discutere e valutare una possibile attività. Tali informazioni confidenziali possono includere, ma non limitare, la ricerca, prodotti, servizi, compilazioni e informazioni tecniche, proprietà tecnologiche, fasi di sviluppo, tecniche di business, invenzioni, processi, informazioni commerciali, dati, liste e prospetti di clienti, liste di consulenti e curriculum vitae e altre, tipo Brevetti, rilevate da terze parti in forma scritta o sotto altre forme tangibili o non tangibili trasmesse verbalmente o visivamente ma identificate riservate all’atto dell’accordo.</p>
      <p>In considerazione del desiderio di ciascuna parte di rilevare come riservate le informazioni di cui sopra, i sottoscriventi si accordano come segue:</p>
      <ul>
        <li>Ricevere e mantenere tutte le informazioni con riservatezza</li>
        <li>Usare queste informazioni solo per lo scopo comune</li>
        <li>Non rilevare alcuna informazione riservata a persone non direttamente o indirettamente collegate allo scopo prefisso senza il consenso dell’altra parte</li>
        <li>Non permettere ad altri atti od azioni che siano vietate da questo accordo</li>
        <li>Non usare informazioni riservate per proprio uso o qualsiasi altro scopo eccetto che per valutare il comune desiderio di svolgere attività in comune</li>
        <li>Operare in buona fede a supporto dell’essenza del rapporto.</li>
      </ul>
      <p>Queste restrizioni di uso e riservatezza non si applicano per quelle informazioni che:</p>
      <ul>
        <li>Sono di pubblico dominio prima dell’accordo</li>
        <li>Sono ricevute da terze parti non soggette ad obbligo di confidenzialità</li>
        <li>Erano conosciute agli scriventi al momento dell’accordo e questa conoscenza può essere dimostrata</li>
        <li>Sussiste un obbligo di legge che vieta la riservatezza.</li>
      </ul>
      <p>Questo accordo sarà effettivo dalla data di sottoscrizione del presente atto e non può durare più di tre anni dalla data stessa. Le parti possono risolvere questo accordo dandone preavviso scritto di 30 giorni lavorativi. Dopo questo termine le informazioni riservate torneranno ad essere di proprietà di ciascuna parte ed ogni documento o file dovrà essere prontamente restituito, insieme alle copie, entro 5 giorni dalla data di scadenza dell’accordo. Nessuna parte di questo accordo e nessun diritto sarà trasferibile senza consenso scritto di entrambe le parti.</p>
    </div>
  </div>

  <div class="section signoff">
    <div class="section__tab" style="width:172px">Letto e accettato da:</div>
    <div class="col col--customer">
      <h4>CUSTOMER</h4>
      <div class="sign-line sign-line--date">Data<span></span></div>
      <div class="sign-line sign-line--sign">Firma<span></span></div>
    </div>
    <div class="col col--vault">
      <h4>LSV</h4>
      Luca Bernardi<br>Amministratore Unico<br>Orbis Data Services srl
      <div class="sign-line sign-line--date">Data<span></span></div>
      <div class="sign-line sign-line--sign">Firma<span></span></div>
    </div>
  </div>

  <footer class="footer">
    <strong>Orbis Data Services srl</strong>, Via Galvani 12/B, 20089 - Rozzano (MI)<br>
    Telefono: <strong>+39 02 55501234</strong><span class="gap"></span>info@loomstorevault.net<span class="gap"></span><strong>www.loomstorevault.net</strong>
  </footer>
</section>

</body>
</html>
```